Flyer für Immobilienmaklerunternehmen
Zielgruppe
Wir sind ein Immobilienmaklerunternehmen in Bochum.
Wir lassen die Flyer in die Briefkästen verteilen.
Wir möchten Eigentümer erreichen und diese am Besten zur Kontaktaufnahme motivieren. Oder zumindest in Erinnerung bleiben.
Viele brauchen unsere Dienstleistungen nur zu einem bestimmten Zeitpunkt.
Unsere Zielgruppe sind meist ältere Eigentümer, die entweder aus Sorge, wegen privatem Stress, Unwissenheit oder Erlösmaximierung einen Makler beauftragen.
Wir würden gerne mit den Flyern diejenigen ansprechen, die Sorge haben und ggf. unwissend sind. Hierbei stellen wir uns einen Flyer vor, der auf der Vorderseite ein Bild mit 'unsicheren Zeiten' nutzt, um Aufmerksamkeit zu erregen (wir haben bspw. einen Flyer mit einem Leuchtturm gesehen, der durch den Sturm den Weg weist, mit dem Spruch' Wir geben Ihnen auch in stürmischen Zeiten eine sichere Orientierung' etwas Ähnliches stellen wir uns vor) mit einem passenden Slogan.
Zudem hätten wir auf der Vorderseite ebenso unser Logo, als auch das Zertifikat.
Auf der Rückseite gerne die Motivation zur Kontaktaufnahme wie oben beschrieben, zudem hatten wir uns eine kurze Vorstellung unserer Dienstleistungen (Verkauf, Wertgutachten, Vermietung, Wohnflächenberechnung und Energieausweis) vorgestellt.
Dann hätten wir entweder gerne ein Teamfoto eingebaut mit Einladung zur Kontaktaufnahme, alternativ unseren Slogan 'Unser Erstgespräch kostet Sie einen Kaffee und einen Keks.' und anstelle des Teamfotos dann einem Bild von Kaffee und Keksen o.Ä.
Die Adressdaten der Firmen bitte sehr dezent/klein plazieren.
Bitte diese beiden Büros einbauen:
Lanberg Immobilien
Molvener Weg 417
44861 Bochum
www.lanberg-immobilien-beispiel.info
und
Kesu Immobilien
Tillweg 27
44627 Herne
www.kesu-beispiel.de
(Bitte die Logos von der Homepage verwenden)
Aufgabenstellung
Unser Logo sollte zu finden sein, sowie die Geschäftsfarben (aus dem Logo)
Zudem muss die Handhabbarkeit beim Verteilen gegeben sein.
Wir kennen uns nicht so gut aus und benötigen am Schluss ein Ergebnis, mit dem wir die Flyer direkt drucken lassen können.
Bei Spezialformaten freuen wir uns, wenn Sie uns sagen, wo man diese drucken lassen kann.

```html
<!DOCTYPE html>
<html lang="de">
<head>
<meta charset="utf-8">
<title>Lanberg Immobilien – Flyer</title>
<link href="https://fonts.googleapis.com/css2?family=Montserrat:wght@400;600;700&family=Source+Sans+3:wght@400;600&display=swap" rel="stylesheet">
<style>
  :root {
    --brand-green: #6aaa38;
    --paper: #f3f3f3;
    --backdrop: #e4e4e4;
    --ink: #2b2b2b;
    --navy: #1f3569;
    --seal-blue: #2f5fa0;
    --partner-grey: #6b6b6b;
    --white: #ffffff;
  }
  * { box-sizing: border-box; margin: 0; padding: 0; }
  html, body { width: 1200px; height: 1200px; overflow: hidden; background: var(--backdrop); }
  .flyer {
    position: absolute; left: 204px; top: 40px;
    width: 792px; height: 1120px;
    background: var(--paper);
    box-shadow: 0 2px 10px rgba(0,0,0,0.12);
    font-family: "Source Sans 3", sans-serif;
    color: var(--ink);
    overflow: hidden;
  }
  .hero { position: absolute; left: 0; top: 0; width: 792px; height: 701px; }
  .brand {
    position: absolute; left: 55px; top: 44px; width: 160px;
    display: flex; align-items: center; gap: 10px;
    font-family: "Montserrat", sans-serif; font-weight: 600;
    color: var(--brand-green); font-size: 19px; line-height: 1.15;
  }
  .brand-square { width: 22px; height: 22px; border: 3px solid var(--brand-green); flex: none; }
  .headline {
    position: absolute; left: 42px; top: 518px;
    font-family: "Montserrat", sans-serif; font-weight: 600;
    font-size: 78px; line-height: 82px; color: var(--white); letter-spacing: 0.3px;
    white-space: nowrap;
  }
  .intro-title {
    position: absolute; left: 44px; top: 728px;
    font-family: "Montserrat", sans-serif; font-weight: 700;
    color: var(--brand-green); font-size: 23px; line-height: 30px; white-space: nowrap;
  }
  .intro-text {
    position: absolute; left: 44px; width: 386px;
    font-size: 17px; line-height: 21.5px; text-align: justify;
  }
  .intro-text.first { top: 768px; }
  .intro-text.second { top: 944px; }
  .cta {
    position: absolute; left: 46px; top: 1032px; width: 239px; height: 52px;
    background: var(--brand-green); color: var(--white);
    font-family: "Montserrat", sans-serif; font-weight: 700; font-size: 14px; line-height: 18.5px;
    padding: 8px 0 0 16px;
  }
  .badge { position: absolute; left: 500px; }
  .membership-text {
    position: absolute; left: 590px; width: 190px;
    font-family: "Montserrat", sans-serif; font-weight: 400;
    font-size: 13.5px; line-height: 17px;
  }
</style>
</head>
<body>
<main class="flyer">
  <svg class="hero" viewBox="0 0 792 701">
    <defs>
      <linearGradient id="photoTone" x1="0" y1="0" x2="1" y2="0.3">
        <stop offset="0" stop-color="#ece6de"/>
        <stop offset="0.45" stop-color="#d9c9b6"/>
        <stop offset="0.7" stop-color="#8a7a6c"/>
        <stop offset="1" stop-color="#1e2430"/>
      </linearGradient>
    </defs>
    <rect x="0" y="372" width="792" height="329" fill="var(--brand-green)"/>
    <path d="M18 21 H774 V378 C720 378 700 400 670 440 C640 480 610 499 560 499 H18 Z" fill="url(#photoTone)" role="img" aria-label="Foto: Händedruck über einem Schreibtisch mit Hausmodell und Taschenrechner"/>
    <path d="M18 21 H272 C232 25 228 120 205 162 C188 190 160 196 18 196 Z" fill="var(--paper)"/>
  </svg>

  <div class="brand">
    <span class="brand-square"></span>
    <span>Lanberg Immobilien</span>
  </div>

  <h1 class="headline">Ihre Immobilie<br>in guten Händen</h1>

  <h2 class="intro-title">Ihre Zufriedenheit ist unser Ziel</h2>
  <p class="intro-text first">Lanberg &amp; Kesu Immobilien - Ihr verlässlicher Partner für Immobilienverkauf, Vermietung, Wertgutachten und Energieausweis in Bochum und Herne. Wir unterstützen Sie gerne dabei, Ihre Immobilie erfolgreich zu verkaufen oder zu vermieten. Vertrauen Sie auf unsere Expertise und unseren persönlichen Service.</p>
  <p class="intro-text second">Kontaktieren Sie uns noch heute und profitieren Sie von unserer langjährigen Erfahrung und unserem individuellen Angebot.</p>

  <div class="cta">Wir begleiten Sie<br>kompetent und persönlich!</div>

  <svg class="badge" style="top:727px" width="60" height="61" viewBox="0 0 60 61"><rect width="60" height="61" fill="var(--navy)"/></svg>
  <div class="membership-text" style="top:727px">Maklerbund<br>Deutschland<br>Mitglied seit 2013</div>

  <svg class="badge" style="top:809px" width="60" height="100" viewBox="0 0 60 100"><path d="M0 0 H60 V72 C60 88 45 100 30 100 C15 100 0 88 0 72 Z" fill="var(--seal-blue)"/></svg>
  <div class="membership-text" style="top:843px">Wir bleiben für Sie<br>auf dem Laufenden!</div>

  <svg class="badge" style="top:925px;left:493px" width="70" height="70" viewBox="0 0 70 70"><circle cx="35" cy="35" r="32" fill="none" stroke="var(--navy)" stroke-width="5"/></svg>
  <div class="membership-text" style="top:932px">Unser Unternehmen<br>erfüllt die Vorschriften<br>der DIN EN 15733 seit 2017</div>

  <svg class="badge" style="top:1014px" width="60" height="58" viewBox="0 0 60 58"><rect width="60" height="58" fill="var(--partner-grey)"/></svg>
  <div class="membership-text" style="top:1010px">Immobilienring<br>Emscher-Ruhr e.V.<br>Partnerschaftlich<br>zum Erfolg!</div>
</main>
</body>
</html>
```